wealth management firm, professional group, new model

we have a logo that works but we need a card, white background using our colors...clean look

our tag line if can be used in

The Road From Member to Partner

```html
<!DOCTYPE html>
<html lang="en">
<head>
<meta charset="utf-8">
<title>Kelvara Wealth Partners – Business Card</title>
<link href="https://fonts.googleapis.com/css2?family=Montserrat:wght@400&family=Poppins:wght@400;500&display=swap" rel="stylesheet">
<style>
  :root{
    --stage:#555555;
    --navy:#15294b;
    --paper:#ffffff;
    --paper-soft:#f3f3f3;
    --mist:#dedede;
    --ink:#1f1f1f;
    --rule:#8a8a8a;
  }
  html,body{margin:0;padding:0;overflow:hidden;}
  body{width:967px;height:1200px;background:var(--stage);position:relative;}
  .card{
    position:absolute;left:91px;width:785px;height:449px;overflow:hidden;
    background:radial-gradient(circle at 80% 25%, var(--paper-soft) 0%, var(--paper) 60%);
    box-shadow:0 4px 18px rgba(0,0,0,.25);
  }
  .card--front{top:105px;}
  .card--back{top:647px;}
  .card__waves{position:absolute;inset:0;width:785px;height:449px;}
  .brand-name{
    position:absolute;margin:0;color:var(--navy);
    font-family:"Montserrat",sans-serif;font-weight:400;
    letter-spacing:.2em;text-transform:uppercase;text-align:center;
  }
  .card--front .brand-name{left:0;right:0;top:148px;font-size:30px;line-height:1.75;}
  .tagline{
    position:absolute;left:0;right:0;top:380px;margin:0;text-align:center;
    color:var(--paper);font-family:"Poppins",sans-serif;font-weight:500;
    font-size:27px;letter-spacing:.14em;text-transform:uppercase;white-space:nowrap;
  }
  .card--back .brand-name{left:54px;width:330px;top:176px;font-size:20px;line-height:1.7;}
  .divider{position:absolute;left:367px;top:86px;width:1px;height:206px;background:var(--rule);}
  .person{position:absolute;left:396px;top:100px;font-family:"Poppins",sans-serif;}
  .person__name{margin:0;color:var(--navy);font-size:33px;font-weight:400;line-height:1.1;}
  .person__role{margin:0;color:var(--ink);font-size:19px;line-height:1.2;}
  .contacts{position:absolute;left:396px;top:175px;margin:0;padding:0;list-style:none;font-family:"Poppins",sans-serif;}
  .contacts li{display:flex;align-items:center;height:27px;margin-bottom:7.5px;color:var(--ink);font-size:20px;}
  .contacts svg{width:27px;height:27px;margin-right:9px;flex:none;}
</style>
</head>
<body>

<section class="card card--front">
  <svg class="card__waves" viewBox="0 0 785 449" aria-hidden="true">
    <path d="M0 198 C120 262 250 312 380 334 L0 334 Z" fill="var(--mist)"/>
    <path d="M0 308 C250 345 500 335 785 210 L785 449 L0 449 Z" fill="var(--navy)"/>
  </svg>
  <p class="brand-name">Kelvara<br>Wealth Partners</p>
  <p class="tagline">The Road From Member to Partner</p>
</section>

<section class="card card--back">
  <svg class="card__waves" viewBox="0 0 785 449" aria-hidden="true">
    <path d="M0 270 C120 320 250 370 370 395 L0 395 Z" fill="var(--mist)"/>
    <path d="M0 373 C250 405 500 397 785 273 L785 449 L0 449 Z" fill="var(--navy)"/>
  </svg>
  <p class="brand-name">Kelvara<br>Wealth Partners</p>
  <div class="divider"></div>
  <div class="person">
    <h1 class="person__name">Maren Castell</h1>
    <p class="person__role">Owner</p>
  </div>
  <ul class="contacts">
    <li>
      <svg viewBox="0 0 27 27" aria-hidden="true"><circle cx="13.5" cy="13.5" r="13.5" fill="var(--navy)"/><path d="M9 7.5c.8-.5 1.6-.2 2 .6l1 2c.3.7.1 1.3-.5 1.7l-.6.4c.6 1.5 1.7 2.7 3.3 3.4l.5-.6c.4-.6 1.1-.8 1.7-.4l2 1.1c.7.4 1 1.2.5 2l-.6.8c-.8 1-2.2 1.2-3.4.6-3-1.5-5.3-3.9-6.6-6.9-.5-1.2-.3-2.6.7-3.4z" fill="#fff"/></svg>
      555.010.2984
    </li>
    <li>
      <svg viewBox="0 0 27 27" aria-hidden="true"><circle cx="13.5" cy="13.5" r="13.5" fill="var(--navy)"/><rect x="7" y="9" width="13" height="9" rx="1" fill="none" stroke="#fff" stroke-width="1.4"/><path d="M7.5 9.5l6 4.5 6-4.5" fill="none" stroke="#fff" stroke-width="1.4"/></svg>
      info@kelvarawealth.com
    </li>
    <li>
      <svg viewBox="0 0 27 27" aria-hidden="true"><circle cx="13.5" cy="13.5" r="13.5" fill="var(--navy)"/><g fill="none" stroke="#fff" stroke-width="1.3"><circle cx="13.5" cy="13.5" r="6.5"/><ellipse cx="13.5" cy="13.5" rx="2.8" ry="6.5"/><path d="M7 13.5h13M8 10h11M8 17h11"/></g></svg>
      www.kelvarawealth.com
    </li>
  </ul>
</section>

</body>
</html>
```